Data Analysis new tech startup

Design a simple / modern website (one page, one language) with a tech touch, based on the words prediction and/or IoT (Internet of Things).

VOLTEQ IoT is dedicated for Data Analysis of IoT or M2M (Machine to Machine) projects.

The website should follow the colors of the logo (see images)

The web site should look like this example: https://malvira-systems.example/en/ with less human pictures and ALL the text content should be configurable for later change.

The website will be published on a php web server.

Target Market(s)

Business professionals

Industry/Entity Type

Data Science

Coding

Coded - Design and coding required

Number of Pages Required

1 page

Colors

Designer to choose colors to be used in the design.

Requirements
Must have
• Follow example site guidelines (https://malvira-systems.example/en/)
• Follow logo colors
• Fun and startup look and feel
• ALL TEXT SHOULD BE CONFIGURABLE
• Clients carrousel with colored hovering
Nice to have
• Configurable photo carrousel at the top (after menu)
Should not have
• Too many human photos, just a few.

```html
<!DOCTYPE html>
<html lang="en">
<head>
<meta charset="utf-8">
<title>VOLTEQ IoT — Connecting Data</title>
<link href="https://fonts.googleapis.com/css2?family=Montserrat:wght@300;400;500&family=Roboto:ital,wght@0,300;0,400;0,500;1,300;1,400&display=swap" rel="stylesheet">
<style>
:root{
  --navy:#262a52;
  --indigo:#3d4790;
  --purple:#7a2db4;
  --cyan:#5fd3ee;
  --lilac:#a78be8;
  --ink:#1d1d1d;
  --muted:#3a3a3a;
  --white:#ffffff;
  --footer:#2b2b2b;
}
*{margin:0;padding:0;box-sizing:border-box}
html,body{width:1200px;height:3286px;overflow:hidden}
body{position:relative;font-family:"Roboto",sans-serif;color:var(--ink);background:var(--white)}
h1,h2,h3{font-weight:400}
.abs{position:absolute}
a{color:inherit;text-decoration:none}

/* hero */
.hero{left:0;top:0;width:1200px;height:672px}
.hero-panel{left:0;top:0;width:459px;height:672px;background:linear-gradient(180deg,#272c58 0%,#2a2f5c 60%,#262a50 100%)}
.hero-visual{left:459px;top:0;width:741px;height:672px;background:radial-gradient(circle at 55% 70%,#c9b4ff 0%,#7a5ad6 14%,#4c4fa8 38%,#3a3f86 62%,#5a3572 100%)}
.brand{font-family:"Montserrat",sans-serif;font-weight:500;color:var(--white);font-size:21px;letter-spacing:.5px;display:flex;align-items:center;gap:8px}
.brand-dot{width:8px;height:8px;background:var(--lilac);border-radius:50%}
.nav{top:48px;left:561px;font-size:12.5px;color:var(--white)}
.nav a{position:absolute;white-space:nowrap}
.nav a.active::after{content:"";position:absolute;left:-3px;right:-3px;bottom:-7px;height:2px;background:var(--white)}
.hero-title{left:92px;top:210px;font-family:"Montserrat",sans-serif;font-weight:300;font-size:42px;line-height:40px;color:var(--white);letter-spacing:1px}
.hero-title .accent{background:linear-gradient(90deg,var(--cyan),var(--lilac));-webkit-background-clip:text;background-clip:text;color:transparent}
.hero-copy{left:96px;top:418px;font-size:10.5px;line-height:16px;color:#c8cbe6}
.btn{display:flex;align-items:center;justify-content:center;gap:8px;width:128px;height:42px;border:1px solid var(--white);color:var(--white);font-size:10px;letter-spacing:.3px}

/* methodology */
.section-title{width:1200px;left:0;text-align:center;font-size:23px;font-weight:400;color:var(--ink)}
.method-lead{left:105px;top:760px;width:990px;text-align:center;font-size:14px;line-height:19px;color:var(--ink);letter-spacing:.3px}
.method-col{width:284px;font-size:11.5px;line-height:14.2px;color:var(--muted);letter-spacing:.4px}
.method-icon{width:60px;height:58px;border-radius:14px}
.method-label{font-family:"Montserrat",sans-serif;font-size:16px;color:#8bb0f0;text-align:center;width:120px}

/* connecting band */
.band{left:0;top:1063px;width:1200px;height:473px;background:radial-gradient(circle at 30% 10%,#5058a6 0%,#3a4190 40%,#2c3170 100%)}
.band-title{left:97px;top:1175px;font-family:"Montserrat",sans-serif;font-weight:300;font-size:38px;color:var(--cyan);letter-spacing:-.5px}
.band-copy{left:96px;top:1238px;width:428px;font-size:19px;line-height:24px;color:var(--white);letter-spacing:-.3px}
.band-visual{left:530px;top:1150px;width:540px;height:310px;border-radius:8px;background:radial-gradient(circle at 45% 55%,#6a4fd0 0%,#4c4aa8 40%,rgba(58,65,144,0) 75%)}

/* offering */
.offer-sub{left:0;top:1620px;width:1200px;text-align:center;font-size:17px;color:var(--ink);letter-spacing:.3px}
.card{top:1682px;width:232px;height:416px;padding:36px 14px 36px 32px;color:var(--white)}
.card h3{font-family:"Montserrat",sans-serif;font-weight:400;font-size:16.5px;line-height:20px;letter-spacing:.2px;white-space:nowrap}
.card .rule{width:24px;height:2px;background:var(--white);margin:12px 0 14px}
.card p{font-size:11.5px;line-height:16.5px;color:#b9c3ee}
.card-consult{left:96px;background:linear-gradient(180deg,#5962a8,#3a4183)}
.card-design{left:354px;background:linear-gradient(180deg,#3e62b6,#3453a0)}
.card-research{left:613px;background:linear-gradient(180deg,#5a3ea8,#4a2f90)}
.card-training{left:872px;background:linear-gradient(180deg,#5f2762,#4e2154)}

/* life */
.video{left:111px;top:2208px;width:433px;height:295px;background:radial-gradient(circle at 70% 40%,#3c6c95 0%,#142434 55%,#0b0f16 100%)}
.video-play{left:190px;top:104px;width:52px;height:52px;border:3px solid var(--white);border-radius:50%}
.video-time{left:196px;top:166px;font-size:13px;color:var(--white)}
.video-bar{left:24px;top:280px;width:395px;height:2px;background:#6c7080}
.video-bar i{display:block;width:185px;height:2px;background:#3e6ad6}
.photo{left:600px;top:2208px;width:504px;height:557px;border-radius:4px;background:linear-gradient(180deg,#dfe4ea 0%,#aebccb 45%,#8b6a52 75%,#5b4536 100%)}
.quote{left:96px;top:2528px;width:190px;font-size:12px;line-height:19px;color:var(--muted);letter-spacing:.4px}
.quote-name{left:98px;top:2642px;font-size:12.5px;font-style:italic;color:#6a86e8}
.quote-role{left:100px;top:2658px;font-size:12.5px;font-style:italic;color:var(--muted)}
.stat{left:302px;top:2523px;width:244px;height:242px;border-radius:4px;background:linear-gradient(135deg,#8fe1f4 0%,#a3c0f4 50%,#b29ff0 100%);color:var(--white);text-align:right;padding:36px 44px 0 0}
.stat .over{font-family:"Montserrat",sans-serif;font-weight:300;font-size:34px;line-height:34px}
.stat .num{font-family:"Montserrat",sans-serif;font-weight:500;font-size:82px;line-height:82px;margin-top:2px}
.stat .unit{font-family:"Montserrat",sans-serif;font-weight:500;font-size:48px;line-height:46px;margin-right:-3px}

/* contact / careers */
.contact{left:0;top:2865px;width:600px;height:266px;background:#272b4e}
.careers{left:600px;top:2865px;width:600px;height:266px;background:var(--purple)}
.block-title{width:600px;left:0;text-align:center;font-size:25px;font-weight:400;color:var(--white)}
.icon-circle{width:80px;height:80px;border-radius:50%;display:flex;align-items:center;justify-content:center}
.careers-lead{top:2962px;width:600px;text-align:center;font-style:italic;font-weight:300;font-size:27px;color:#e6d8ff}
.careers-copy{top:2993px;width:600px;text-align:center;font-size:17px;line-height:24px;color:#f0e6ff;font-weight:300}

/* footer */
.footer{left:0;top:3190px;width:1200px;height:96px;background:var(--footer);color:var(--white)}
.footer-links{left:322px;top:32px;display:flex;gap:22px;font-size:10px;letter-spacing:-.3px}
.footer-meta{font-size:9px;color:#9a9a9a}
</style>
</head>
<body>

<header class="abs hero">
  <div class="abs hero-panel"></div>
  <div class="abs hero-visual" role="img" aria-label="Hand holding a smartphone projecting a glowing wireframe network of data points"></div>
  <div class="abs brand" style="left:97px;top:42px">VOLTEQ IoT<span class="brand-dot"></span></div>
  <nav class="abs nav">
    <a style="left:0">Our Methodology</a>
    <a class="active" style="left:143px">Our Offering</a>
    <a style="left:255px">Careers</a>
    <a style="left:351px">Life at Volteq</a>
    <a style="left:473px">Contact</a>
  </nav>
  <h1 class="abs hero-title">LEADING<br>THE WORLD'S<br><span class="accent">CONECTING<br>DATA</span></h1>
  <p class="abs hero-copy">Lorem ipsum dolor sit amet<br>Lorem ipsum dolor sit amet, consectetur adipiscing elit.</p>
  <a class="abs btn" style="left:97px;top:480px">WATCH NOW
    <svg width="14" height="6" viewBox="0 0 14 6"><path d="M0 3h12M10 1l2 2-2 2" stroke="#fff" fill="none"/></svg></a>
</header>

<section>
  <h2 class="abs section-title" style="top:720px">Our Methodology</h2>
  <p class="abs method-lead">Lorem ipsum dolor sit amet, consectetur adipiscing elit. Phasellus eget felis condimentum, hendrerit ipsum quis, iaculis lectus. Phasellus vitae felis vitae metus lacinia imperdiet. Praesent nec odio quis nisi laoreet volutpat et ac dolor.</p>

  <div class="abs method-icon" role="img" aria-label="Learn symbol" style="left:203px;top:818px;background:linear-gradient(135deg,#3a6ad8,#5fd3ee)"></div>
  <div class="abs method-label" style="left:172px;top:876px">Learn</div>
  <p class="abs method-col" style="left:96px;top:904px">Lorem ipsum dolor sit amet, consectetur adipiscing elit. Phasellus eget felis condimentum, hendrerit ipsum quis, iaculis lectus. Phasellus vitae felis vitae metus lacinia imperdiet. Praesent nec odio quis nisi laoreet volutpat et ac dolor. Morbi mi felis, posuere vitae feugiat eu,</p>

  <div class="abs method-icon" role="img" aria-label="Apply symbol" style="left:577px;top:818px;background:linear-gradient(135deg,#3a6ad8,#9a6ee8)"></div>
  <div class="abs method-label" style="left:546px;top:881px">Apply</div>
  <p class="abs method-col" style="left:464px;top:906px">Lorem ipsum dolor sit amet, consectetur adipiscing elit. Phasellus eget felis condimentum, hendrerit ipsum quis, iaculis lectus. Phasellus vitae felis vitae metus lacinia imperdiet. Praesent nec odio quis nisi laoreet volutpat et ac dolor. Morbi mi felis, posuere vitae feugiat eu,</p>

  <div class="abs method-icon" role="img" aria-label="Manage symbol" style="left:920px;top:822px;width:96px;background:linear-gradient(90deg,#3a6ad8,#b94ad0)"></div>
  <div class="abs method-label" style="left:908px;top:881px">Manage</div>
  <p class="abs method-col" style="left:823px;top:906px">Lorem ipsum dolor sit amet, consectetur adipiscing elit. Phasellus eget felis condimentum, hendrerit ipsum quis, iaculis lectus. Phasellus vitae felis vitae metus lacinia imperdiet. Praesent nec odio quis nisi laoreet volutpat et ac dolor. Morbi mi felis, posuere vitae feugiat eu,</p>
</section>

<section>
  <div class="abs band"></div>
  <h2 class="abs band-title">CONECTING DATA</h2>
  <p class="abs band-copy">Lorem ipsum dolor sit amet, consectetur. Lorem ipsum dolor sit amet, consectetur adipiscing elit.Lorem ipsum dolor sit amet, consectetur adipiscing elit.</p>
  <a class="abs btn" style="left:97px;top:1377px">WATCH NOW
    <svg width="14" height="6" viewBox="0 0 14 6"><path d="M0 3h12M10 1l2 2-2 2" stroke="#fff" fill="none"/></svg></a>
  <div class="abs band-visual" role="img" aria-label="Isometric laptop with data screen surrounded by bar charts, a lightbulb, a padlock and a monitor"></div>
</section>

<section>
  <h2 class="abs section-title" style="top:1585px">Our Offering</h2>
  <p class="abs offer-sub">Lorem ipsum dolor sit amet, consectetur adipiscing elit.</p>

  <article class="abs card card-consult" role="img" aria-label="Businesswoman facing a digital interface, blue tint">
    <h3>CONSULTING<br>&amp; IMPLEMENTATION</h3><div class="rule"></div>
    <p>Definition of the Data strategy<br>Definition of the Data strategy<br>Definition of the Data strategy.</p>
  </article>
  <article class="abs card card-design" role="img" aria-label="Low-poly sculpture on a desk, blue tint">
    <h3>DESIGN &amp;<br>DEVELOPMENT</h3><div class="rule"></div>
  </article>
  <article class="abs card card-research" role="img" aria-label="Hands working on a tablet, violet tint">
    <h3>RESEACH<br>&amp; DEVELOPMENT</h3><div class="rule"></div>
  </article>
  <article class="abs card card-training" role="img" aria-label="Hand-drawn quality growth chart, plum tint">
    <h3>TRAINING<br>&amp; COACHING</h3><div class="rule"></div>
  </article>
</section>

<section>
  <h2 class="abs section-title" style="top:2147px">Life at Volteq</h2>
  <div class="abs video" role="img" aria-label="Video still of a hand holding a key in a beam of light">
    <div class="abs video-play"><svg width="46" height="46" viewBox="0 0 46 46"><path d="M18 14l14 9-14 9z" fill="#fff"/></svg></div>
    <div class="abs video-time">55 : 04</div>
    <div class="abs video-bar"><i></i></div>
  </div>
  <div class="abs photo" role="img" aria-label="Team meeting around a long conference table in a bright office"></div>
  <p class="abs quote">Lorem ipsum dolor sit amet, consectetur adipiscing elit. Donec ut ipsum eu lorem ornare vestibulum et ut metus. Fusce sit amet quam erat.</p>
  <div class="abs quote-name">Maren Castillo</div>
  <div class="abs quote-role">/ President</div>
  <div class="abs stat"><div class="over">Over</div><div class="num">50</div><div class="unit">clients</div></div>
</section>

<section>
  <div class="abs contact">
    <h2 class="abs block-title" style="top:54px;left:-8px">CONTACT US</h2>
    <div class="abs icon-circle" style="left:143px;top:105px;background:#3e63b8">
      <svg width="40" height="40" viewBox="0 0 40 40" fill="none" stroke="#fff" stroke-width="1.6"><circle cx="20" cy="14" r="6"/><circle cx="20" cy="14" r="2"/><path d="M6 30l8-5h10l-4 3h-6M22 28l10-6 3 3-11 9H8"/></svg></div>
    <div class="abs icon-circle" style="left:262px;top:105px;background:#7b7b7b">
      <svg width="40" height="40" viewBox="0 0 40 40" fill="none" stroke="#fff" stroke-width="1.6"><rect x="8" y="8" width="24" height="24" rx="2"/><circle cx="20" cy="20" r="6"/><circle cx="20" cy="20" r="2"/></svg></div>
    <div class="abs icon-circle" style="left:376px;top:105px;background:#7b2f6a">
      <svg width="40" height="40" viewBox="0 0 40 40" fill="none" stroke="#fff" stroke-width="1.6"><path d="M8 20l12-10 12 10M12 18v12h16V18"/><rect x="17" y="22" width="6" height="8"/></svg></div>
  </div>
  <div class="abs careers">
    <h2 class="abs block-title" style="top:54px">CAREERS</h2>
  </div>
  <p class="abs careers-lead" style="left:600px">Join VOLTEQ IoT</p>
  <p class="abs careers-copy" style="left:600px">We attach as much importance to our company<br>culture as we do to our data expertise.</p>
  <a class="abs btn" style="left:842px;top:3049px">APPLY NOW
    <svg width="14" height="6" viewBox="0 0 14 6"><path d="M0 3h12M10 1l2 2-2 2" stroke="#fff" fill="none"/></svg></a>
</section>

<footer class="abs footer">
  <div class="abs brand" style="left:134px;top:30px">VOLTEQ IoT<span class="brand-dot"></span></div>
  <div class="abs footer-links"><a>About Us</a><a>Term of Uses</a><a>Privacy Policy</a></div>
  <div class="abs footer-meta" style="left:322px;top:50px">Address : 123.....</div>
  <div class="abs footer-meta" style="left:460px;top:50px">Phone number:</div>
  <div class="abs footer-meta" style="left:578px;top:50px">Email:</div>
  <div class="abs footer-meta" style="left:322px;top:66px">COPYRIGHT(C) ABC. ALL RIGHT RESERVED.</div>
</footer>

</body>
</html>
```